Wellspring Care Alliance Vonzo Ads

We want an ad created for the gay dating app vonzo. The size is 300x250. We want the ad to be sexy, with a shirtless man. We are advertising our free HIV and PrEP services. We are open to slogans about maybe "Bringing HIV and PrEP To You"
"Free PrEP and HIV Management"
Open to ideas.

We also offer through the Harborlight Support Fund
Copay Assistance, Insurance Premium Assistance, Free Medical Services, etc
Our website is wcanj.org

I do want the ad to have a Book Now Button

Gay sexually active males

```html
<!DOCTYPE html>
<html lang="en">
<head>
<meta charset="utf-8">
<title>Wellspring Care Alliance – Vonzo Ad</title>
<link rel="stylesheet" href="https://fonts.googleapis.com/css2?family=Poppins:wght@400;500;600;700&display=swap">
<style>
  :root {
    --page: #dcdcdc;
    --ink-dark: #0b0a12;
    --glow-blue: #3b3fc4;
    --glow-violet: #2a1b5e;
    --white: #ffffff;
    --black: #111111;
    --blue: #4f6bff;
    --violet: #8f4dff;
    --pink: #ff4fa8;
    --magenta: #d94bff;
    --brand: #7a3cf0;
  }
  * { margin: 0; padding: 0; box-sizing: border-box; }
  html, body {
    width: 1200px; height: 1040px; overflow: hidden;
    background: var(--page);
    font-family: "Poppins", sans-serif;
  }
  .ad {
    position: absolute; left: 0; top: 20px;
    width: 1200px; height: 1000px; overflow: hidden;
    background:
      radial-gradient(ellipse 620px 520px at 0 0, var(--glow-blue) 0%, rgba(59,63,196,0.45) 35%, rgba(42,27,94,0) 75%),
      radial-gradient(ellipse 500px 400px at 1100px 80px, rgba(120,50,200,0.35), rgba(0,0,0,0) 70%),
      var(--ink-dark);
  }
  .ad-art { position: absolute; inset: 0; }
  .headline {
    position: absolute; left: 60px; top: 62px;
    color: var(--white);
    font-weight: 600; font-size: 84px; line-height: 110px;
    letter-spacing: 0.5px;
  }
  .headline .accent {
    background: linear-gradient(90deg, var(--blue), var(--violet) 60%, var(--magenta));
    -webkit-background-clip: text; background-clip: text; color: transparent;
  }
  .benefits {
    position: absolute; left: 56px; top: 331px;
    list-style: none; color: var(--white);
    font-size: 38px; font-weight: 400; line-height: 50px;
  }
  .benefits li { position: relative; padding-left: 56px; margin-bottom: 18px; }
  .benefits .tick { position: absolute; left: 0; top: 9px; width: 32px; height: 32px; }
  .book-now {
    position: absolute; left: 56px; top: 804px;
    width: 458px; height: 76px; border-radius: 38px;
    background: linear-gradient(90deg, var(--blue), var(--violet) 55%, var(--pink));
    color: var(--white); font-weight: 700; font-size: 46px;
    display: flex; align-items: center; justify-content: center;
    letter-spacing: 0.5px;
  }
  .website {
    position: absolute; left: 106px; top: 905px;
    color: var(--black); font-size: 46px; font-weight: 400; line-height: 60px;
  }
  .website b { font-weight: 700; }
  .brand {
    position: absolute; left: 760px; top: 830px;
    display: flex; align-items: center; gap: 22px;
  }
  .brand-dot { width: 84px; height: 84px; border-radius: 50%; background: var(--brand); flex: none; }
  .brand-name {
    color: var(--brand); font-weight: 600; font-size: 36px; line-height: 42px;
    text-transform: uppercase; letter-spacing: 1px;
  }
</style>
</head>
<body>
<main class="ad">
  <svg class="ad-art" width="1200" height="1000" viewBox="0 0 1200 1000">
    <defs>
      <radialGradient id="photo-tone" cx="930" cy="500" r="400" gradientUnits="userSpaceOnUse">
        <stop offset="0" stop-color="#b57e60"/>
        <stop offset="0.35" stop-color="#6e4636"/>
        <stop offset="0.75" stop-color="#241820"/>
        <stop offset="1" stop-color="#0e0b12" stop-opacity="0"/>
      </radialGradient>
      <linearGradient id="arc-top" x1="892" y1="104" x2="1346" y2="558" gradientUnits="userSpaceOnUse">
        <stop offset="0" stop-color="#7b4dff"/>
        <stop offset="0.5" stop-color="#c44bff"/>
        <stop offset="1" stop-color="#ff4fa8"/>
      </linearGradient>
      <linearGradient id="arc-side" x1="592" y1="356" x2="708" y2="790" gradientUnits="userSpaceOnUse">
        <stop offset="0" stop-color="#3f5bff"/>
        <stop offset="1" stop-color="#5a7bff"/>
      </linearGradient>
    </defs>
    <circle cx="960" cy="490" r="384" fill="url(#photo-tone)" role="img" aria-label="Photo of a shirtless man lying on a bed, seen from behind"/>
    <path d="M892 104 A392 392 0 0 1 1346 558" fill="none" stroke="url(#arc-top)" stroke-width="12" stroke-linecap="round"/>
    <path d="M592 356 A392 392 0 0 0 708 790" fill="none" stroke="url(#arc-side)" stroke-width="12" stroke-linecap="round"/>
    <path d="M0 886 L620 886 C700 886 700 780 790 780 L1200 780 L1200 1000 L0 1000 Z" fill="#ffffff"/>
  </svg>

  <h1 class="headline">BRINGING <span class="accent">HIV</span><br>AND <span class="accent">PREP</span> TO YOU</h1>

  <ul class="benefits">
    <li><svg class="tick" viewBox="0 0 32 32"><circle cx="16" cy="16" r="13" fill="none" stroke="#ffffff" stroke-width="3"/><path d="M9.5 16.5 L14.5 21 L23.5 10.5" fill="none" stroke="#b45cff" stroke-width="3.5" stroke-linecap="round" stroke-linejoin="round"/></svg>Harborlight Support<br>Fund</li>
    <li><svg class="tick" viewBox="0 0 32 32"><circle cx="16" cy="16" r="13" fill="none" stroke="#ffffff" stroke-width="3"/><path d="M9.5 16.5 L14.5 21 L23.5 10.5" fill="none" stroke="#b45cff" stroke-width="3.5" stroke-linecap="round" stroke-linejoin="round"/></svg>Copay Assistance</li>
    <li><svg class="tick" viewBox="0 0 32 32"><circle cx="16" cy="16" r="13" fill="none" stroke="#ffffff" stroke-width="3"/><path d="M9.5 16.5 L14.5 21 L23.5 10.5" fill="none" stroke="#b45cff" stroke-width="3.5" stroke-linecap="round" stroke-linejoin="round"/></svg>Insurance Premium<br>Assistance</li>
    <li><svg class="tick" viewBox="0 0 32 32"><circle cx="16" cy="16" r="13" fill="none" stroke="#ffffff" stroke-width="3"/><path d="M9.5 16.5 L14.5 21 L23.5 10.5" fill="none" stroke="#b45cff" stroke-width="3.5" stroke-linecap="round" stroke-linejoin="round"/></svg>Free Medical Services</li>
  </ul>

  <div class="book-now">BOOK NOW</div>
  <p class="website">www.<b>wcanj</b>.org</p>

  <div class="brand">
    <span class="brand-dot"></span>
    <span class="brand-name">Wellspring<br>Care Alliance</span>
  </div>
</main>
</body>
</html>
```